I need a business card design for a new company that will be doing consulting work around issues of cultural competency, and diversity and inclusion. I would like the design to be crisp and clear with bold but conservative colors and incorporate shades of blue

Target Market(s)

Small businesses, schools, non-profits

Industry/Entity Type

Consulting

Font styles to use
Serif
Sans Serif

Colors
0c5ba6
6b449b
3276b5
0292cd

Requirements
Must have
• A Morrow Venture (name of company)
• Lemlem Tavish
• CEO
• lemlem@amorrowventure.com
• (215)483-2756

```html
<!DOCTYPE html>
<html lang="en">
<head>
<meta charset="utf-8">
<title>A Morrow Venture — Business Card</title>
<link rel="stylesheet" href="https://fonts.googleapis.com/css2?family=Cinzel:wght@500&family=Open+Sans:wght@400&display=swap">
<style>
  :root {
    --page-bg: #efefef;
    --card-bg: #ffffff;
    --brand-blue: #0c5ba6;
    --brand-mid: #3276b5;
    --map-tint: #cfe2f5;
    --map-tint-soft: #e6f0fa;
    --ink: #1d1d1f;
    --hairline: #e9edf2;
  }
  * { margin: 0; padding: 0; box-sizing: border-box; }
  html, body {
    width: 1200px;
    height: 985px;
    overflow: hidden;
    background: var(--page-bg);
  }
  .card {
    position: absolute;
    left: 160px;
    top: 219px;
    width: 841px;
    height: 504px;
    background: var(--card-bg);
    box-shadow: 0 1px 3px rgba(0,0,0,0.08);
    overflow: hidden;
  }
  .top-rule {
    position: absolute;
    left: 82px;
    right: 0;
    top: 70px;
    height: 1px;
    background: var(--hairline);
  }
  .world-map {
    position: absolute;
    left: 95px;
    top: 94px;
    width: 686px;
    height: 386px;
    border-radius: 40% 45% 35% 40%;
    background: radial-gradient(ellipse at 55% 40%, var(--map-tint) 0%, var(--map-tint-soft) 55%, rgba(255,255,255,0) 78%);
    opacity: 0.8;
  }
  .person {
    position: absolute;
    right: 64px;
    top: 98px;
    text-align: right;
  }
  .person-name {
    font-family: "Cinzel", Georgia, serif;
    font-weight: 500;
    font-size: 30px;
    color: var(--brand-blue);
    line-height: 1;
    letter-spacing: 0.5px;
  }
  .person-title {
    margin-top: 10px;
    font-family: "Open Sans", Arial, sans-serif;
    font-size: 16px;
    color: var(--ink);
  }
  .brand {
    position: absolute;
    right: 64px;
    top: 320px;
    display: flex;
    align-items: center;
    gap: 18px;
  }
  .brand-mark {
    width: 14px;
    height: 14px;
    background: var(--brand-blue);
  }
  .brand-text { text-align: right; }
  .brand-name {
    font-family: "Cinzel", Georgia, serif;
    font-weight: 500;
    font-size: 36px;
    color: var(--brand-blue);
    line-height: 1;
    letter-spacing: 1px;
  }
  .brand-tagline {
    margin-top: 6px;
    font-family: "Open Sans", Arial, sans-serif;
    font-size: 11.5px;
    letter-spacing: 3.2px;
    color: var(--ink);
  }
  .accent-band {
    position: absolute;
    left: 82px;
    right: 0;
    top: 397px;
    height: 4px;
    background: linear-gradient(to right, rgba(12,91,166,0) 0%, var(--brand-mid) 35%, var(--brand-blue) 100%);
  }
  .contact {
    position: absolute;
    right: 64px;
    top: 410px;
    display: flex;
    align-items: center;
    font-family: "Open Sans", Arial, sans-serif;
    font-size: 18px;
    color: var(--ink);
  }
  .contact-item { display: flex; align-items: center; gap: 7px; }
  .contact-icon { fill: var(--brand-blue); }
  .contact-divider {
    width: 2px;
    height: 26px;
    background: var(--ink);
    margin: 0 10px;
  }
</style>
</head>
<body>
  <main class="card">
    <div class="top-rule"></div>
    <div class="world-map" role="img" aria-label="Dotted world map in pale blue"></div>

    <div class="person">
      <p class="person-name">Lemlem Tavish</p>
      <p class="person-title">CEO</p>
    </div>

    <div class="brand">
      <span class="brand-mark"></span>
      <div class="brand-text">
        <p class="brand-name">A Morrow Venture</p>
        <p class="brand-tagline">INCLUSIVE INSIGHT · PRACTICAL GUIDANCE</p>
      </div>
    </div>

    <div class="accent-band"></div>

    <div class="contact">
      <span class="contact-item">
        <svg class="contact-icon" width="18" height="16" viewBox="0 0 18 16" aria-hidden="true">
          <path d="M1 5 C1 1.5 17 1.5 17 5 L17 6.5 L13 6.5 L13 4.8 C11 4 7 4 5 4.8 L5 6.5 L1 6.5 Z"/>
          <path d="M4 8 L14 8 L16 15 L2 15 Z"/>
          <circle cx="9" cy="11.3" r="1.8" fill="#fff"/>
        </svg>
        (215)483-2756
      </span>
      <span class="contact-divider"></span>
      <span class="contact-item">
        <svg class="contact-icon" width="18" height="13" viewBox="0 0 18 13" aria-hidden="true">
          <rect x="0" y="0" width="18" height="13"/>
          <path d="M1 1 L9 7.5 L17 1" fill="none" stroke="#fff" stroke-width="1.5"/>
        </svg>
        lemlem@amorrowventure.com
      </span>
    </div>
  </main>
</body>
</html>
```